New modern and elegant label for Pisco La Cumbrera

Currently our supplier from Pisco La Cumbrera has a old-fashioned label. My distributors and clients have the opinion that the label blocks their sales, and I agree.
So I am looking for a modern, new label for these bottles. Basically I would let you be free in your design.
Pisco is a grape distillate, at about 40% alc. vol., origin is Peru.
La Cumbrera is a classic pisco producer, so that can be reflected in the label. The label itself doesnt have to be the same as it has been, otherwise shaped labels are fine too.
Attached, the current bottles (500ml and 700ml), also an image on how a clean 500ml bottle looks like.
Please surprise us, don't be shy in going in an a-typical way. Make your design shine!!!
Target Market(s)
Cocktail makers, end users, distrubutors, clients of liquor stores
Industry/Entity Type
Sales
Requirements
Must have
- A clean, modern look, whilst still connecting to the classicness of the brand La Cumbrera
Nice to have
- As an example of something different I put the Santa Brisa label idea. Modern, elegant and still classic. Not saying I want something like that literally, but could be used as a guideline on ideas

```html
<!DOCTYPE html>
<html lang="es">
<head>
<meta charset="utf-8">
<title>Pisco La Cumbrera – Etiqueta</title>
<link rel="stylesheet" href="https://fonts.googleapis.com/css2?family=Libre+Baskerville&family=Great+Vibes&family=Dancing+Script&display=swap">
<style>
  :root {
    --page: #ffffff;
    --label: #e4e4e5;
    --ink: #1d1d1f;
    --grape: #7d3a7a;
    --flag-red: #c8202f;
    --flag-white: #ffffff;
  }
  html, body {
    margin: 0;
    padding: 0;
    width: 1200px;
    height: 800px;
    overflow: hidden;
    background: var(--page);
  }
  .canvas {
    position: relative;
    width: 1200px;
    height: 800px;
  }
  .label-shape {
    position: absolute;
    left: 390px;
    top: 70px;
    width: 420px;
    height: 660px;
  }
  .label-content {
    position: absolute;
    left: 390px;
    top: 70px;
    width: 420px;
    height: 660px;
    text-align: center;
    color: var(--ink);
  }
  .grape-emblem {
    position: absolute;
    left: 160px;
    top: 40px;
    width: 100px;
    height: 150px;
    background: radial-gradient(circle at 50% 45%, var(--grape), #9b5a97);
    border-radius: 40% 40% 50% 50% / 30% 30% 70% 70%;
    opacity: 0.9;
  }
  .brand-name {
    position: absolute;
    top: 255px;
    left: 0;
    width: 100%;
    margin: 0;
    font-family: "Libre Baskerville", serif;
    font-weight: 400;
    font-size: 30px;
    letter-spacing: 6px;
  }
  .product-type {
    position: absolute;
    top: 318px;
    left: 0;
    width: 100%;
  }
  .product-type .pisco {
    display: block;
    font-family: "Great Vibes", cursive;
    font-size: 40px;
    line-height: 36px;
    margin-left: -60px;
  }
  .product-type .origin {
    display: block;
    font-family: "Libre Baskerville", serif;
    font-size: 11px;
    line-height: 13px;
    letter-spacing: 0.3px;
    text-transform: uppercase;
  }
  .flag {
    position: absolute;
    top: 402px;
    left: 202px;
    display: flex;
    width: 16px;
    height: 10px;
  }
  .flag span { flex: 1; }
  .flag .red { background: var(--flag-red); }
  .flag .white { background: var(--flag-white); }
  .variety {
    position: absolute;
    top: 475px;
    left: 0;
    width: 100%;
    font-family: "Dancing Script", cursive;
    font-size: 32px;
    line-height: 36px;
    color: var(--grape);
  }
  .specs {
    position: absolute;
    top: 575px;
    left: 0;
    width: 100%;
    font-family: "Libre Baskerville", serif;
    font-size: 11px;
    line-height: 14px;
  }
</style>
</head>
<body>
<main class="canvas">
  <svg class="label-shape" viewBox="0 0 420 660" aria-hidden="true">
    <polygon points="0,0 420,0 420,560 210,660 0,560" fill="var(--label)"/>
  </svg>
  <section class="label-content">
    <div class="grape-emblem" role="img" aria-label="Grape cluster with vine leaf emblem in purple"></div>
    <h1 class="brand-name">LA CUMBRERA</h1>
    <p class="product-type" style="margin:0">
      <span class="pisco">Pisco</span>
      <span class="origin">De cepas iqueñas<br>tradicionales</span>
    </p>
    <div class="flag" aria-label="Perú">
      <span class="red"></span><span class="white"></span><span class="red"></span>
    </div>
    <p class="variety" style="margin:0">Puro<br>Quebranta</p>
    <p class="specs" style="margin:0">Alc. 40% Vol.<br>500 ml</p>
  </section>
</main>
</body>
</html>
```